Wine Label designs

I need a nice- upper class wine label made. I would like a black or dark background matte finish with gold foil text and the outline. 1583 in the middle in bold & gold. I want to it be Fairhaven themed. With the Ray Hollins fist or beacon of Fairhaven statue or both small in a step and repeat embossed black on the matte black label. All of the label with fists. The name of the brand is 1583. The name comes from when Fairhaven was founded. This label will be for a red win.

Target Market(s)

Wine drinkers & Fairhaven Michigan themed background

Industry/Entity Type

Wine

Logo Text

1583

Logo styles of interest
Wordmark Logo
Requirements
Must have
• The color Gold
Nice to have
• Matte finish and Gold out line & gold text

```html
<!DOCTYPE html>
<html lang="en">
<head>
<meta charset="utf-8">
<title>1583 Red Wine Label</title>
<link href="https://fonts.googleapis.com/css2?family=DM+Serif+Display&display=swap" rel="stylesheet">
<style>
  :root {
    --page: #ffffff;
    --label-black: #262626;
    --foil-gold: #c89f65;
    --emboss-grey: #6b6b6b;
    --art-grey: #595959;
  }
  * { margin: 0; padding: 0; box-sizing: border-box; }
  html, body {
    width: 1200px;
    height: 848px;
    overflow: hidden;
    background: var(--page);
  }
  .canvas {
    position: relative;
    width: 1200px;
    height: 848px;
  }
  .wine-label {
    position: absolute;
    left: 385px;
    top: 85px;
    width: 430px;
    height: 677px;
    background: var(--label-black);
    font-family: "DM Serif Display", serif;
  }
  .label-art {
    position: absolute;
    left: 60px;
    top: 22px;
    width: 311px;
    height: 280px;
    background: linear-gradient(180deg, #3a3a3a 0%, var(--art-grey) 55%, #4a4a4a 100%);
  }
  .gold-frame {
    position: absolute;
    inset: 0;
    width: 430px;
    height: 677px;
  }
  .gold-frame line {
    stroke: var(--foil-gold);
    stroke-width: 1.6;
  }
  .brand-number {
    position: absolute;
    left: 0;
    right: 0;
    top: 338px;
    text-align: center;
    font-size: 168px;
    font-weight: 400;
    line-height: 1;
    letter-spacing: -7px;
    color: var(--foil-gold);
    text-shadow: -5px 4px 0 var(--emboss-grey);
  }
  .wine-type {
    position: absolute;
    left: 0;
    right: 0;
    top: 541px;
    text-align: center;
    font-size: 31px;
    line-height: 1;
    color: var(--emboss-grey);
  }
  .wine-origin {
    position: absolute;
    left: 0;
    right: 0;
    top: 577px;
    text-align: center;
    font-size: 25px;
    line-height: 1;
    color: var(--emboss-grey);
  }
</style>
</head>
<body>
<main class="canvas">
  <section class="wine-label">
    <div class="label-art" role="img" aria-label="Grey engraved-style illustration in the label's top area"></div>
    <svg class="gold-frame" viewBox="0 0 430 677" aria-hidden="true">
      <line x1="29" y1="44.5" x2="179" y2="44.5"/>
      <line x1="251" y1="44.5" x2="400" y2="44.5"/>
      <line x1="29" y1="44.5" x2="29" y2="649"/>
      <line x1="400" y1="44.5" x2="400" y2="649"/>
      <line x1="29" y1="649" x2="400" y2="649"/>
      <line x1="39" y1="55" x2="179" y2="55"/>
      <line x1="251" y1="55" x2="390.5" y2="55"/>
      <line x1="39" y1="55" x2="39" y2="639"/>
      <line x1="390.5" y1="55" x2="390.5" y2="639"/>
      <line x1="39" y1="639" x2="390.5" y2="639"/>
    </svg>
    <h1 class="brand-number">1583</h1>
    <p class="wine-type">Red Wine</p>
    <p class="wine-origin">~ Fairhaven ~</p>
  </section>
</main>
</body>
</html>
```